Velmar Ops Business Cards

We need to design some upbeat business cards. We are an Industrial Rope Access Company/Height Safety Company that specialize in Rope Access, Confined Space, Anchor Points, Safety Systems, PPE Inspecions and Rigging.
Company name is Velmar Ops Ltd
Card is for Gareth Lomas the Company Director
His mobile number is 027 418 9072 and email is gareth@velmarops.co.nz. Website address is www.velmarops.co.nz.
We will post some pictures below to ensure you get a good idea of what we do.

```html
<!DOCTYPE html>
<html lang="en">
<head>
<meta charset="utf-8">
<title>Velmar Ops Business Cards</title>
<link rel="stylesheet" href="https://fonts.googleapis.com/css2?family=Jost:wght@400;500;700&display=swap">
<style>
  :root {
    --page-bg: #c4c3bd;
    --card-navy: #2d2e5e;
    --rule-blue: #3d4f9e;
    --ink-white: #ffffff;
    --ink-soft: #e6e7f2;
  }
  * { margin: 0; padding: 0; box-sizing: border-box; }
  html, body {
    width: 1200px; height: 900px; overflow: hidden;
    background: var(--page-bg);
    font-family: "Jost", sans-serif;
  }
  .canvas { position: relative; width: 1200px; height: 900px; }
  .card {
    position: absolute; top: 302px;
    width: 470px; height: 296px;
    background: var(--card-navy);
    border-radius: 18px;
    overflow: hidden;
    color: var(--ink-white);
  }
  .card--front { left: 98px; }
  .card--back { left: 628px; }

  /* Front */
  .front-rule {
    position: absolute; top: 147px; height: 3px; background: var(--rule-blue);
  }
  .front-rule--left { left: 0; width: 92px; }
  .front-rule--right { right: 0; width: 92px; }
  .front-brand {
    position: absolute; left: 0; right: 0; top: 120px;
    text-align: center;
    font-weight: 700; font-size: 40px; line-height: 56px; letter-spacing: 1px;
  }
  .front-web {
    position: absolute; left: 0; right: 0; top: 174px;
    display: flex; justify-content: center; align-items: center; gap: 5px;
    font-size: 14px; color: var(--ink-soft);
  }

  /* Back */
  .holder-name {
    position: absolute; left: 27px; top: 46px;
    font-weight: 700; font-size: 20px; letter-spacing: 0.4px; text-transform: uppercase;
  }
  .holder-title {
    position: absolute; left: 27px; top: 73px;
    font-size: 14px; letter-spacing: 0.3px; text-transform: uppercase; color: var(--ink-soft);
  }
  .back-rule { position: absolute; top: 103px; height: 3px; background: var(--ink-white); }
  .back-rule--long { left: 0; width: 292px; }
  .back-rule--short { right: 0; width: 16px; }
  .back-brand {
    position: absolute; left: 298px; width: 152px; top: 89px;
    text-align: center;
    font-weight: 700; font-size: 22px; line-height: 30px; letter-spacing: 0.5px;
  }
  .contact-list { position: absolute; left: 26px; top: 202px; list-style: none; }
  .contact-item {
    display: flex; align-items: center; gap: 16px;
    height: 25.5px; font-size: 14px; color: var(--ink-soft);
  }
  .contact-icon { width: 18px; height: 18px; flex: none; }
</style>
</head>
<body>
<main class="canvas">
  <section class="card card--front" aria-label="Card front">
    <div class="front-rule front-rule--left"></div>
    <div class="front-rule front-rule--right"></div>
    <div class="front-brand">Velmar Ops</div>
    <div class="front-web">
      <svg width="11" height="11" viewBox="0 0 24 24" fill="none" stroke="currentColor" stroke-width="2">
        <circle cx="12" cy="12" r="10"/><ellipse cx="12" cy="12" rx="4" ry="10"/><path d="M2 12h20M4 7h16M4 17h16"/>
      </svg>
      <span>www.velmarops.co.nz</span>
    </div>
  </section>

  <section class="card card--back" aria-label="Card back">
    <h1 class="holder-name">Gareth Lomas</h1>
    <p class="holder-title">The Director</p>
    <div class="back-rule back-rule--long"></div>
    <div class="back-brand">Velmar Ops</div>
    <div class="back-rule back-rule--short"></div>
    <ul class="contact-list">
      <li class="contact-item">
        <svg class="contact-icon" viewBox="0 0 24 24" fill="none" stroke="currentColor" stroke-width="1.5" stroke-linejoin="round">
          <path d="M5 3l4 1 1 5-2 1.5a11 11 0 0 0 5.5 5.5L15 14l5 1 1 4-2 2C10 21 3 14 3 5z"/>
          <path d="M14 3a7 7 0 0 1 7 7M14 6.5a3.5 3.5 0 0 1 3.5 3.5"/>
        </svg>
        <span>027 418 9072</span>
      </li>
      <li class="contact-item">
        <svg class="contact-icon" viewBox="0 0 24 24" fill="none" stroke="currentColor" stroke-width="1.5">
          <circle cx="12" cy="12" r="9.5"/><ellipse cx="12" cy="12" rx="4" ry="9.5"/><path d="M2.5 12h19M4 7.5h16M4 16.5h16"/>
        </svg>
        <span>www.velmarops.co.nz</span>
      </li>
      <li class="contact-item">
        <svg class="contact-icon" viewBox="0 0 24 24" fill="none" stroke="currentColor" stroke-width="1.5" stroke-linejoin="round">
          <rect x="2.5" y="5" width="19" height="14"/><path d="M2.5 5l9.5 8 9.5-8M2.5 19l7-7M21.5 19l-7-7"/>
        </svg>
        <span>gareth@velmarops.co.nz</span>
      </li>
    </ul>
  </section>
</main>
</body>
</html>
```